QuillBackDesk Website Redesign

I'm looking to redesign our website QuillBackDesk.com. The main goal is to give it a fresh design that is easy on the eyes and pushes the users to creating an account.

Our platform is very simple and we only do one thing, we use ai to generate response to customer and product reviews.

See attached file to see the pricing section style.

On the homepage just under the hero section, I would like to include the wording:
"Write replies to the reviews you get on sites like:" then show the logos like we have on our register page: https://app.quillbackdesk.com/public/index.php

Target Market(s)

Business owners with brick and morter business or any business or product that gets online reviews

Industry/Entity Type

reputation management

Number of Pages Required

2 page

Requirements
Must have
• Home page and pricing page

```html
<!DOCTYPE html>
<html lang="en">
<head>
<meta charset="utf-8">
<title>QuillBackDesk – AI replies to your reviews</title>
<link rel="stylesheet" href="https://fonts.googleapis.com/css2?family=Poppins:wght@400;500;600;700;800&display=swap">
<style>
:root{
  --blue:#2144a3;
  --blue-dark:#172f7a;
  --navy:#1a1f3d;
  --orange:#f7a81b;
  --orange-deep:#f08c12;
  --lilac:#e9e8f8;
  --grey:#6d7287;
  --line:#d9dbe6;
  --white:#ffffff;
}
*{box-sizing:border-box;margin:0;padding:0}
html,body{width:1200px;height:4012px;overflow:hidden}
body{font-family:"Poppins",sans-serif;color:var(--navy);background:var(--white);position:relative}
.abs{position:absolute}
.accent{color:var(--orange)}

/* nav */
.brand{display:flex;align-items:center;gap:10px;font-weight:700;color:var(--blue);font-size:26px;white-space:nowrap}
.brand-mark{width:34px;height:34px;border-radius:8px;background:var(--blue)}
.nav{left:0;top:0;width:1200px;height:90px}
.nav .brand{position:absolute;left:128px;top:24px}
.nav-links{position:absolute;left:520px;top:36px;display:flex;gap:24px;font-size:11px;font-weight:600;letter-spacing:.4px;white-space:nowrap}
.nav-links a{color:var(--navy);text-decoration:none}
.nav-links a.active{color:var(--orange)}
.btn{display:inline-flex;align-items:center;gap:8px;font-size:12px;font-weight:700;border-radius:6px;padding:0 18px;height:38px;text-decoration:none;white-space:nowrap}
.btn-outline{border:2px solid var(--navy);color:var(--navy);background:var(--white)}
.btn-orange{background:var(--orange);color:var(--white)}
.nav .btn{position:absolute;left:995px;top:25px}

/* hero */
.hero-blob{left:560px;top:30px}
.hero-title{left:88px;top:236px;width:520px;font-size:40px;line-height:1.2;font-weight:800}
.hero-actions{left:88px;top:504px;display:flex;gap:16px}
.hero-art{left:640px;top:70px;width:500px;height:620px;border-radius:44% 44% 40% 40%;background:linear-gradient(160deg,#f4c84a 0%,#e9e8f8 60%,#2144a3 100%)}

/* logos */
.sites-title{left:0;top:740px;width:1200px;text-align:center;font-size:26px;font-weight:700;line-height:1.35}
.sites{left:150px;top:830px;width:900px;display:flex;justify-content:space-between}
.site{width:104px;height:104px;border-radius:50%;background:#f1f1f4;display:flex;align-items:center;justify-content:center;font-size:14px;font-weight:600;color:var(--navy)}

/* blue band */
.band-title{left:0;top:1196px;width:1200px;text-align:center;color:var(--white);font-size:28px;font-weight:700;line-height:1.3}
.band-sub{left:0;top:1330px;width:1200px;text-align:center;color:var(--white);font-size:18px;font-weight:600}
.diamond{left:310px;top:1410px;width:270px;height:270px;background:var(--orange);border-radius:40px;transform:rotate(45deg)}
.review-card{left:210px;top:1404px;width:380px;height:280px;background:var(--white);border-radius:12px;box-shadow:0 18px 40px rgba(10,20,60,.25);padding:24px 24px 0 28px}
.reviewer{display:flex;gap:14px;align-items:center}
.avatar{width:62px;height:62px;border-radius:8px;background:#c9ccd9}
.reviewer-name{font-size:15px;font-weight:700}
.reviewer-meta{font-size:10px;color:var(--grey)}
.stars{color:var(--orange);font-size:13px;letter-spacing:1px}
.review-text{margin-top:14px;background:#f2f5ff;border-radius:6px;padding:12px;font-size:10.5px;line-height:1.55;color:#3a3f58}
.reply-text{margin-top:10px;margin-left:40px;background:#fff7e6;border-radius:6px;padding:10px;font-size:10.5px;line-height:1.5;color:#3a3f58}
.card-btn{position:absolute;left:28px;bottom:-14px;background:var(--blue);color:var(--white);font-size:10px;font-weight:600;padding:8px 14px;border-radius:6px}
.quote{left:560px;top:1640px;width:64px;height:64px;border-radius:50%;background:var(--white);box-shadow:0 8px 20px rgba(0,0,0,.15);display:flex;align-items:center;justify-content:center;font-size:40px;font-weight:800;color:var(--blue);line-height:1}
.trust{left:720px;top:1420px;width:320px;color:var(--white)}
.trust h3{font-size:22px;font-weight:700;margin-bottom:12px}
.trust p{font-size:13px;line-height:1.6;opacity:.9}
.arrows{display:flex;gap:12px;margin-top:22px}
.arrow-btn{width:40px;height:40px;border-radius:50%;background:rgba(255,255,255,.2);display:flex;align-items:center;justify-content:center}
.review-site{left:120px;top:1800px;display:flex;align-items:center;gap:10px;font-size:30px;font-weight:700;color:var(--navy)}
.review-site span.dot{width:22px;height:22px;border-radius:50%;background:#d1d3de}

/* how it works */
.how-title{left:0;top:1942px;width:1200px;text-align:center;font-size:30px;font-weight:700}
.timeline{left:599px;top:2080px;width:2px;height:620px;background:var(--line)}
.step-num{width:76px;height:76px;border-radius:50%;color:var(--white);font-weight:700;font-size:20px;display:flex;align-items:center;justify-content:center;border:8px solid #eef0f7}
.n1{left:562px;top:2094px;background:var(--blue-dark)}
.n2{left:562px;top:2354px;background:var(--orange)}
.n3{left:562px;top:2604px;background:var(--blue)}
.step{width:400px}
.step .kicker{font-size:12px;font-weight:600;margin-bottom:6px}
.step h4{font-size:20px;font-weight:700;margin-bottom:8px}
.step p{font-size:11.5px;line-height:1.6;color:var(--grey)}
.step.left{left:140px;text-align:right}
.step.right{left:672px}
.step-art{width:150px;height:130px;border-radius:18px;background:linear-gradient(135deg,#e6e9f7,#c8cdea)}

/* faq */
.faq-title{left:80px;top:2868px;font-size:30px;font-weight:700}
.faq-list{left:80px;top:2976px;width:712px;display:flex;flex-direction:column;gap:20px}
.faq-item{height:56px;border-radius:6px;background:var(--white);box-shadow:0 6px 20px rgba(26,31,61,.1);display:flex;align-items:center;justify-content:space-between;padding:0 22px;font-size:12px;font-weight:600}
.faq-item .plus{color:var(--orange);font-size:20px;font-weight:700}
.faq-person{left:800px;top:2770px;width:320px;height:600px;border-radius:160px 160px 0 0;background:linear-gradient(180deg,#e4e6f2 0%,#9fb0d9 70%,#2b3f7d 100%)}

/* cta */
.cta{left:80px;top:3436px;width:1040px;height:210px;background:var(--orange);border-radius:16px;padding:54px 70px;color:var(--white)}
.cta h2{font-size:30px;font-weight:700}
.cta p{font-size:14px;margin-top:6px}
.cta .btn{position:absolute;right:70px;top:88px;background:var(--white);color:var(--navy)}

/* footer */
.footer-brand{left:130px;top:3820px}
.footer-brand .brand{color:var(--white);font-size:30px}
.footer-brand .brand-mark{background:var(--white)}
.fcol{top:3790px;color:var(--white)}
.fcol h5{font-size:16px;font-weight:700;margin-bottom:12px}
.fcol li{list-style:none;font-size:12px;line-height:2;opacity:.9}
.socials{display:flex;gap:12px}
.social{width:36px;height:36px;border-radius:50%;background:rgba(255,255,255,.25)}
.copy{left:0;top:3978px;width:1200px;text-align:center;color:var(--white);font-size:11px;opacity:.85}
.to-top{left:1140px;top:3960px;width:38px;height:38px;border-radius:50%;background:var(--orange)}
</style>
</head>
<body>

<svg class="abs hero-blob" width="640" height="760" viewBox="0 0 640 760" aria-hidden="true">
  <path d="M120 40 C260 -20 520 0 620 120 L640 760 L0 760 C60 620 40 520 80 420 C110 300 20 120 120 40Z" fill="#f3f2fb"/>
</svg>
<svg class="abs" style="left:0;top:930px" width="1200" height="900" viewBox="0 0 1200 900" aria-hidden="true">
  <path d="M0 120 C260 0 520 200 800 120 C980 70 1100 20 1200 60 L1200 790 C1000 860 760 750 520 810 C300 860 120 840 0 790Z" fill="var(--blue)"/>
  <path d="M0 180 C280 60 540 260 820 170 C1000 110 1110 80 1200 110 L1200 130 C1100 100 1000 130 820 190 C540 280 280 80 0 200Z" fill="#3a5cc0" opacity=".6"/>
</svg>
<svg class="abs" style="left:0;top:3560px" width="1200" height="452" viewBox="0 0 1200 452" aria-hidden="true">
  <path d="M0 120 C240 40 420 160 640 110 C860 60 1020 20 1200 80 L1200 452 L0 452Z" fill="var(--blue)"/>
</svg>

<header class="abs nav">
  <div class="brand"><span class="brand-mark"></span>QuillBackDesk</div>
  <nav class="nav-links">
    <a class="active" href="#">HOME</a><a href="#">WHY REPLY?</a><a href="#">HOW IT WORKS</a><a href="#">PRICING</a><a href="#">BLOG</a><a href="#">LOGIN</a>
  </nav>
  <a class="btn btn-outline" href="#">TRY FREE ›</a>
</header>

<h1 class="abs hero-title">Write personalized<br>responses to <span class="accent">reviews</span><br>in 10 seconds!<br>(NO JOKE)</h1>
<div class="abs hero-actions">
  <a class="btn btn-orange" href="#">START FOR FREE ›</a>
  <a class="btn btn-outline" href="#">LEARN MORE ›</a>
</div>
<div class="abs hero-art" role="img" aria-label="Illustration of a smiling woman holding a phone, surrounded by review site badges and a small profile card"></div>

<h2 class="abs sites-title">Write replies to the <span class="accent">reviews</span><br>you get on sites like</h2>
<div class="abs sites">
  <div class="site">Parcelo</div><div class="site">Searchly</div><div class="site">Trustvane</div><div class="site">Staynest</div><div class="site">Wayfarely</div><div class="site">Craftory</div><div class="site">Nearbly</div>
</div>

<h2 class="abs band-title">It's simple. Our tool writes replies<br>and responses to the <span class="accent">reviews</span> your<br>customers leave.</h2>
<p class="abs band-sub">Doesn't matter if it's 1 or 5 stars.</p>
<div class="abs diamond"></div>
<article class="abs review-card">
  <div class="reviewer">
    <div class="avatar" role="img" aria-label="Reviewer portrait"></div>
    <div>
      <div class="reviewer-name">Corin</div>
      <div class="reviewer-meta">Local Guide · 12 reviews</div>
      <div class="stars">★★★★☆</div>
    </div>
  </div>
  <p class="review-text">Decent food. I've been here a few times, and each time service was slow. Staff are friendly though and the dessert is still worth the wait.</p>
  <p class="reply-text">Thank you for bringing this to our attention, Corin. We're sorry to hear you've had a slow visit.</p>
  <span class="card-btn">Your First Reply is Free</span>
</article>
<div class="abs quote">”</div>
<div class="abs trust">
  <h3>Build Customer Trust</h3>
  <p>Customers want to know there are humans behind your business. Show them you care and value every word they leave.</p>
  <div class="arrows">
    <span class="arrow-btn"><svg width="14" height="14" viewBox="0 0 14 14"><path d="M9 2 L4 7 L9 12" stroke="#fff" stroke-width="2" fill="none"/></svg></span>
    <span class="arrow-btn"><svg width="14" height="14" viewBox="0 0 14 14"><path d="M5 2 L10 7 L5 12" stroke="#fff" stroke-width="2" fill="none"/></svg></span>
  </div>
</div>
<div class="abs review-site">Nearbly<span class="dot"></span></div>

<h2 class="abs how-title">How <span class="accent">it</span> works</h2>
<div class="abs timeline"></div>

<div class="abs step left" style="top:2080px">
  <div class="kicker">Create An Account</div>
  <h4>1 minute account creation</h4>
  <p>Gain access to the most powerful tool for writing unique and personal responses to the reviews your customers leave your business.</p>
</div>
<div class="abs step-num n1">01</div>
<div class="abs step-art" style="left:690px;top:2070px" role="img" aria-label="Illustration of a person setting up an account at a desk"></div>

<div class="abs step-art" style="left:360px;top:2330px" role="img" aria-label="Illustration of review cards being copied and pasted"></div>
<div class="abs step-num n2">02</div>
<div class="abs step right" style="top:2340px">
  <div class="kicker">Copy And Paste The Review</div>
  <h4>We make it way too simple!</h4>
  <p>Just copy the customer review and paste it into your account dashboard.</p>
</div>

<div class="abs step left" style="top:2590px">
  <div class="kicker">Personalized Response In Seconds</div>
  <h4>Only a 10 second wait</h4>
  <p>In just seconds you'll receive 3 unique and personal responses. Choose the reply you like best or tell our system to generate 3 more.</p>
</div>
<div class="abs step-num n3">03</div>
<div class="abs step-art" style="left:690px;top:2580px" role="img" aria-label="Illustration of a calendar and clock showing quick turnaround"></div>

<h2 class="abs faq-title">Frequently <span class="accent">Asked</span> Question</h2>
<div class="abs faq-list">
  <div class="faq-item">Why is it important to respond to Searchly reviews?<span class="plus">+</span></div>
  <div class="faq-item">Why is it important to respond to negative reviews?<span class="plus">+</span></div>
  <div class="faq-item">How can I trust someone who doesn't work at my business to reply to reviews on my behalf?<span class="plus">+</span></div>
  <div class="faq-item">Which online review sites does QuillBackDesk.com support?<span class="plus">+</span></div>
</div>
<div class="abs faq-person" role="img" aria-label="Photo of a smiling businessman in glasses and a tie"></div>

<section class="abs cta">
  <h2>Ready to give QuillBackDesk a try?</h2>
  <p>Get started today with one FREE Reply to your Review. No credit card required.</p>
  <a class="btn" href="#">TRY FOR FREE ›</a>
</section>

<div class="abs footer-brand"><div class="brand"><span class="brand-mark"></span>QuillBackDesk</div></div>
<div class="abs fcol" style="left:600px">
  <h5>Quick Links</h5>
  <ul><li>Why Reply?</li><li>How It Works</li><li>Pricing</li><li>Latest Blog</li><li>Login</li></ul>
</div>
<div class="abs fcol" style="left:780px">
  <h5>Information</h5>
  <ul><li>Blog</li><li>Privacy Policy</li><li>Contact</li><li>Sitemap</li></ul>
</div>
<div class="abs fcol" style="left:940px">
  <h5>Stay Connected</h5>
  <div class="socials"><span class="social"></span><span class="social"></span><span class="social"></span><span class="social"></span></div>
</div>
<p class="abs copy">©2020 quillbackdesk. All Rights reserved</p>
<div class="abs to-top"></div>

</body>
</html>
```